Allied Health Clinic needs catchy poster ad for lightbox

We need a catchy and effective poster designed for our retail lightbox which is in a busy corridor. We are a multi disciplinary sports injury clinic offering a range of allied health services. Established in 1999. We need people to understand our business identity and services clearly. I have come up with a very rough idea as far as what I think the copy should contain. The picture is an example of what image I am trying to convey to the potential client. I am not a designer clearly. We specialise in treating difficult problems.
Size of the poster is 451mm x 741mm at 300dpi. We will then blow the image up to double this size which will be good enough resolution for the printing.

Target Market(s)

White collar professionals - male and female, active 20-50 range

Industry/Entity Type

Healthcare

Font styles to use
Sans Serif

Requirements
Nice to have
• Easy to read, polished, nice tie in to my logo colours

```html
<!DOCTYPE html>
<html lang="en">
<head>
<meta charset="utf-8">
<title>Corelign Physiotherapy – Injury Experts</title>
<link rel="stylesheet" href="https://fonts.googleapis.com/css2?family=Anton&family=Lato:wght@400;700;900&family=Roboto+Condensed:wght@700;800&display=swap">
<style>
  :root {
    --green: #8cc63f;
    --charcoal: #474747;
    --white: #ffffff;
    --stage: #ffffff;
    --photo-dark: #2b3347;
    --photo-light: #d9d4cf;
  }
  * { margin: 0; padding: 0; box-sizing: border-box; }
  html, body { width: 890px; height: 1200px; overflow: hidden; background: var(--stage); }
  .poster {
    position: absolute; left: 100px; top: 32px; width: 690px; height: 1134px;
    background: var(--white); overflow: hidden;
    font-family: "Lato", sans-serif; color: var(--charcoal);
  }
  .poster > * { position: absolute; }
  .brand-dot { left: 150px; top: 30px; width: 56px; height: 56px; border-radius: 50%; background: var(--green); }
  .brand-name {
    left: 222px; top: 44px; font-family: "Lato", sans-serif; font-weight: 700;
    font-size: 21px; letter-spacing: 0.5px; color: var(--charcoal); line-height: 1.2;
  }
  .brand-name span { display: block; font-size: 11px; letter-spacing: 5.2px; margin-top: 3px; }
  .headline { left: 0; top: 0; }
  .trusted {
    left: 52px; top: 470px; font-family: "Lato", sans-serif; font-weight: 700;
    font-size: 33px; letter-spacing: -0.3px;
  }
  .athletes-band { left: 50px; top: 517px; width: 430px; height: 88px; background: var(--green); }
  .athletes {
    left: 90px; top: 515px; font-family: "Roboto Condensed", sans-serif; font-weight: 700;
    font-size: 84px; line-height: 92px; color: var(--white); letter-spacing: 0.5px;
  }
  .services-title {
    left: 52px; top: 626px; font-family: "Roboto Condensed", sans-serif; font-weight: 700;
    font-size: 31px; line-height: 36px; color: var(--green);
  }
  .service-list { left: 52px; top: 714px; list-style: none; font-size: 18.5px; font-weight: 700; line-height: 22px; }
  .service-list li { display: flex; align-items: flex-start; margin-bottom: 11px; }
  .service-list svg { width: 16px; height: 18px; margin-right: 6px; margin-top: 2px; flex: none; }
  .player-photo {
    left: 270px; top: 430px; width: 420px; height: 700px;
    background: radial-gradient(ellipse at 62% 45%, var(--photo-dark) 0%, #5a6170 35%, var(--photo-light) 62%, rgba(255,255,255,0) 80%);
  }
  .swoosh { left: 0; top: 0; }
  .badge { left: 530px; top: 762px; width: 148px; height: 148px; }
  .badge-text {
    left: 530px; top: 790px; width: 148px; text-align: center; color: var(--white);
    font-size: 11px; font-weight: 700; line-height: 14px;
  }
  .badge-text .since { display: block; color: var(--green); font-size: 19px; line-height: 22px; margin-top: 8px; }
  .badge-text .year { display: block; color: var(--green); font-family: "Roboto Condensed", sans-serif; font-size: 32px; line-height: 32px; }
  .contact { left: 54px; top: 1032px; }
  .contact .directions { font-family: "Roboto Condensed", sans-serif; font-weight: 800; font-size: 31px; line-height: 34px; color: var(--charcoal); }
  .contact .phone { font-family: "Roboto Condensed", sans-serif; font-weight: 700; font-size: 28px; line-height: 30px; color: var(--white); }
  .contact .web { font-size: 19px; line-height: 24px; color: var(--white); }
</style>
</head>
<body>
<main class="poster">
  <div class="player-photo" role="img" aria-label="Photo of a footballer in a navy shirt and white shorts mid-kick, striking a ball"></div>

  <svg class="swoosh" width="690" height="1134" viewBox="0 0 690 1134" aria-hidden="true">
    <path d="M0,984 Q420,950 690,688 L690,716 Q430,975 0,996 Z" fill="var(--charcoal)"/>
    <path d="M0,1004 Q430,975 690,752 L690,1134 L0,1134 Z" fill="var(--green)"/>
  </svg>

  <div class="brand-dot"></div>
  <div class="brand-name">CORELIGN PHYSIOTHERAPY<span>&amp; SPORTS INJURY CLINIC</span></div>

  <svg class="headline" width="690" height="460" viewBox="0 0 690 460">
    <text x="52" y="292" font-family="Anton, sans-serif" font-size="218" fill="var(--charcoal)" textLength="606" lengthAdjust="spacingAndGlyphs">INJURY</text>
    <text x="52" y="441" font-family="Roboto Condensed, sans-serif" font-weight="700" font-size="170" fill="var(--green)" textLength="596" lengthAdjust="spacingAndGlyphs">EXPERTS</text>
  </svg>

  <div class="trusted">TRUSTED BY</div>
  <div class="athletes-band"></div>
  <div class="athletes">ATHLETES</div>

  <h2 class="services-title">A Complete range<br>of services</h2>
  <ul class="service-list">
    <li><svg viewBox="0 0 16 18"><circle cx="8" cy="6" r="5" fill="none" stroke="var(--green)" stroke-width="2"/><path d="M4 17 L8 11 L12 17" fill="none" stroke="var(--green)" stroke-width="2"/></svg>Sports physiotherapy</li>
    <li><svg viewBox="0 0 16 18"><path d="M2 17 Q1 6 5 2 Q8 8 6 17 Z M10 17 Q8 8 11 2 Q15 6 14 17 Z" fill="var(--green)"/></svg>Massage</li>
    <li><svg viewBox="0 0 16 18"><ellipse cx="5" cy="10" rx="3.5" ry="7" fill="var(--green)"/><ellipse cx="11.5" cy="10" rx="3.5" ry="7" fill="var(--green)"/></svg>Podiatry</li>
    <li><svg viewBox="0 0 16 18"><circle cx="11" cy="3" r="2.2" fill="var(--green)"/><path d="M3 9 L7 6 L10 9 L13 9 M7 6 L6 12 L2 16 M6 12 L10 13 L11 17" fill="none" stroke="var(--green)" stroke-width="1.8"/></svg>Exercise<br>physiology</li>
    <li><svg viewBox="0 0 16 18"><circle cx="8" cy="3" r="2.5" fill="var(--green)"/><rect x="5" y="6" width="6" height="11" rx="2" fill="var(--green)"/></svg>Chiropractic</li>
  </ul>

  <svg class="badge" viewBox="0 0 148 148" aria-hidden="true">
    <circle cx="74" cy="74" r="73" fill="var(--green)"/>
    <circle cx="74" cy="74" r="69" fill="var(--white)"/>
    <circle cx="74" cy="74" r="65" fill="var(--charcoal)"/>
  </svg>
  <div class="badge-text">SUCCESSFULLY<br>TREATING<br>DIFFICULT INJURIES<span class="since">SINCE</span><span class="year">1999</span></div>

  <div class="contact">
    <p class="directions">TAKE LIFTS TO LEVEL 8</p>
    <p class="phone">8540 2716</p>
    <p class="web">corelignphysio.com.au</p>
  </div>
</main>
</body>
</html>
```